Business cards for law firm with global theme

I'd like business cards with contact info for two offices. They should include the colors and font of the new logo design, which is a stylized globe with an "F" in it. The feel should be very modern and professional.

```html
<!DOCTYPE html>
<html lang="en">
<head>
<meta charset="utf-8">
<title>Valerin Law – Business Cards</title>
<link href="https://fonts.googleapis.com/css2?family=Montserrat:wght@400;500;700&display=swap" rel="stylesheet">
<style>
  :root {
    --navy: #163b6d;
    --navy-deep: #12315c;
    --sky: #2ea9e0;
    --white: #ffffff;
    --backdrop: #26272a;
  }
  * { margin: 0; padding: 0; box-sizing: border-box; }
  html, body {
    width: 1200px; height: 900px; overflow: hidden;
    background: var(--backdrop);
    font-family: "Montserrat", sans-serif;
  }
  .card {
    position: absolute; left: 250px;
    width: 700px; height: 400px;
    border-radius: 18px; overflow: hidden;
    box-shadow: 0 10px 30px rgba(0,0,0,.45);
  }
  .card--front { top: 30px; background: var(--navy); }
  .card--back { top: 470px; background: var(--white); }

  .brand { position: absolute; display: flex; align-items: center; gap: 22px; }
  .brand__dot { width: 84px; height: 84px; border-radius: 50%; background: var(--sky); flex: none; }
  .brand__name { font-weight: 700; font-size: 46px; letter-spacing: 1px; line-height: 1; white-space: nowrap; }

  .card--front .brand { left: 50%; top: 50%; transform: translate(-50%, -50%); }
  .card--front .brand__name { color: var(--white); }

  .card--back .brand {
    left: 0; top: 0; width: 340px; height: 400px;
    flex-direction: column; justify-content: center; gap: 20px;
  }
  .card--back .brand__dot { width: 78px; height: 78px; }
  .card--back .brand__name { color: var(--navy); font-size: 36px; }

  .details {
    position: absolute; right: 0; top: 0; width: 360px; height: 400px;
    background: var(--navy); color: var(--white);
    padding: 40px 40px 0 54px;
  }
  .details__stripe {
    position: absolute; left: 0; top: 40px; width: 14px; height: 300px;
    background: var(--sky);
  }
  .details__name { color: var(--sky); font-weight: 700; font-size: 26px; letter-spacing: 1px; text-transform: uppercase; line-height: 1.2; }
  .details__role { font-size: 15px; margin-top: 4px; }
  .details__rule { height: 1px; background: var(--sky); margin: 14px 0; width: 250px; }
  .offices { display: flex; flex-direction: column; gap: 10px; }
  .details__address { font-size: 14px; line-height: 1.45; }
  .contacts { list-style: none; font-size: 14px; line-height: 1.75; }
  .contacts li { display: flex; align-items: center; gap: 8px; }
  .contacts svg { width: 12px; height: 12px; flex: none; }
</style>
</head>
<body>
  <section class="card card--front">
    <div class="brand">
      <span class="brand__dot"></span>
      <span class="brand__name">VALERIN LAW</span>
    </div>
  </section>

  <section class="card card--back">
    <div class="brand">
      <span class="brand__dot"></span>
      <span class="brand__name">VALERIN LAW</span>
    </div>
    <div class="details">
      <span class="details__stripe"></span>
      <h1 class="details__name">Daniel Carter</h1>
      <p class="details__role">Managing Director</p>
      <div class="details__rule"></div>
      <div class="offices">
        <p class="details__address">318 Harbor Lane<br>Westfield ON 2046</p>
        <p class="details__address">72 Linden Avenue<br>Brookmere ON 3159</p>
      </div>
      <div class="details__rule"></div>
      <ul class="contacts">
        <li>
          <svg viewBox="0 0 12 12"><path d="M2.5 1 L4.5 1 L5.2 3.6 L4 4.6 C4.7 6 6 7.3 7.4 8 L8.4 6.8 L11 7.5 L11 9.5 C11 10.3 10.3 11 9.5 11 C5 11 1 7 1 2.5 C1 1.7 1.7 1 2.5 1 Z" fill="#2ea9e0"/></svg>
          (555) 284-6310
        </li>
        <li>
          <svg viewBox="0 0 12 12"><rect x="0.5" y="2" width="11" height="8" rx="1" fill="#2ea9e0"/><path d="M1 2.6 L6 6.4 L11 2.6" stroke="#163b6d" stroke-width="1" fill="none"/></svg>
          info@valerinlaw.com
        </li>
        <li>
          <svg viewBox="0 0 12 12"><circle cx="6" cy="6" r="5" fill="none" stroke="#2ea9e0" stroke-width="1.2"/><ellipse cx="6" cy="6" rx="2.2" ry="5" fill="none" stroke="#2ea9e0" stroke-width="1"/><path d="M1 6 H11" stroke="#2ea9e0" stroke-width="1"/></svg>
          www.valerinlaw.com
        </li>
      </ul>
    </div>
  </section>
</body>
</html>
```